Pagina Casalúmen

The Casalúmen is a company dealing with leasing and selling real estate. The current site can be accessed at www.casalumen.com.br. We intend to redesign the look of the site and for that we would like to redesign the home page and the page with information and pictures of the property. The homepage should maintain the characteristics of the current common design simple, short and straightforward. The page with the data of the properties should be accessed with two changes page as it is currently running. The search from the map by region and should be maintained.
The page containing the information of the property will provide a total of 15 small pictures that when clicked will appear in larger size. The colors to be used should be orange, blue, black and white. The map can be maintained in the current colors.
Updates

Payment guaranteed. Deadline for submission of designs April 27.

Industry/Entity Type

Real Estate

Requirements
Must have
• Search by map regions and search box
address
keep colors from the current page
phones
clean look
Nice to have
• clean look
Should not have
• We like the current page. We just want to make it compatible with modern and new design trends and monitors.

```html
<!DOCTYPE html>
<html lang="pt-BR">
<head>
<meta charset="utf-8">
<title>Casalúmen – Busca de imóveis</title>
<link rel="stylesheet" href="https://fonts.googleapis.com/css2?family=Open+Sans:wght@400;600;700&display=swap">
<style>
:root{
  --orange:#f27e05;
  --orange-light:#ffb21f;
  --orange-dark:#e06e00;
  --navy:#2d4a74;
  --navy-deep:#1f3a62;
  --ink:#333;
  --blue-title:#2b4a7c;
  --line:#d5d9e3;
  --muted:#9fb3d2;
  --foot-link:#b6c6de;
  --page:#f3f4f6;
}
*{box-sizing:border-box;margin:0;padding:0}
html,body{width:1200px;height:924px;overflow:hidden;background:var(--page);font-family:"Open Sans",Arial,sans-serif;color:var(--ink)}
.canvas{position:relative;width:1200px;height:924px;overflow:hidden}
.map-bg{position:absolute;left:0;top:0;width:1200px;height:732px;background:radial-gradient(ellipse at 70% 30%,#e6e8ec 0%,#f1f2f4 45%,#f7f7f8 100%)}
.abs{position:absolute}
.top-links{left:986px;top:7px;font-size:11px;color:#333}
.top-links span{margin:0 4px;color:#888}
/* sidebar */
.sidebar{left:140px;top:0;width:239px;height:562px;background:var(--orange)}
.sidebar-shadow{left:125px;top:568px;width:270px;height:18px;border-radius:50%;background:radial-gradient(ellipse at center,rgba(0,0,0,.28),rgba(0,0,0,0) 70%)}
.brand{left:130px;top:29px;width:258px;height:89px;background:#fff;box-shadow:0 3px 6px rgba(0,0,0,.12);display:flex;align-items:center;justify-content:center;gap:9px}
.brand-mark{width:14px;height:14px;background:var(--orange)}
.brand-name{font-size:25px;font-weight:700;color:var(--navy)}
.side-menu{left:158px;top:172px;list-style:none}
.side-menu li{height:28px;font-size:15px;font-weight:600;color:#fff;text-shadow:0 1px 1px rgba(0,0,0,.35);display:flex;align-items:center}
.side-menu li::before{content:"";border-left:5px solid #fff;border-top:3.5px solid transparent;border-bottom:3.5px solid transparent;margin-right:11px}
.side-divider{left:140px;top:457px;width:239px;height:2px;background:rgba(0,0,0,.1);border-bottom:1px solid rgba(255,255,255,.2)}
.phones{left:211px;top:495px;font-size:17px;font-weight:700;color:#fff;line-height:22px;text-shadow:0 1px 1px rgba(0,0,0,.3)}
.phone-icon{left:160px;top:496px}
/* search */
.search{left:397px;top:29px;width:665px;height:238px;background:#fff;border:1px solid var(--line)}
.s-title{font-size:14px;color:var(--blue-title);font-weight:600}
.field{height:26px;border:1px solid #cfd4dc;border-radius:3px;background:#fff;font-size:11px;color:#999;padding-left:9px;display:flex;align-items:center}
.caret{position:absolute;right:0;top:0;width:24px;height:24px;border-left:1px solid #dde;display:flex;align-items:center;justify-content:center}
.caret::after{content:"";border-top:5px solid #555;border-left:4px solid transparent;border-right:4px solid transparent}
.label{font-size:13px;color:#333}
.check{width:14px;height:14px;border:1px solid #c5ccd6;border-radius:3px;background:#fff}
.check.on{background:#4ba3dc;border-color:#3b87bd}
.btn{height:26px;border-radius:3px;background:linear-gradient(#ffbd2a,var(--orange));border:1px solid var(--orange-dark);color:#fff;font-weight:700;font-size:15px;display:flex;align-items:center;justify-content:center;gap:7px;text-shadow:0 1px 1px rgba(0,0,0,.25)}
.s-sep{left:414px;top:117px;width:630px;height:1px;background:#dfe2e8}
/* results */
.results-bar{left:397px;top:281px;width:665px;height:30px;background:var(--navy);color:#fff;font-size:14px;font-weight:600;padding-left:9px;display:flex;align-items:center}
.results-bar b{color:#a9bedb;margin-right:4px}
.card{width:322px;height:121px;background:#fff;border:1px solid var(--line)}
.card.active{background:#e9eef6;border-color:#c4cfe0}
.card.active::after{content:"";position:absolute;right:-1px;top:-1px;width:4px;height:121px;background:var(--navy)}
.photo{position:absolute;left:15px;top:13px;width:134px;height:89px;border:1px solid #ccd;padding:2px;background:#fff;overflow:hidden}
.photo div{width:100%;height:100%;background:linear-gradient(180deg,#a9c6e6 0%,#cfdbe4 35%,#d8c6a6 55%,#6f8a55 80%,#7a7a70 100%)}
.ribbon{position:absolute;right:-1px;top:-1px}
.info{position:absolute;left:161px;top:10px;font-size:12.5px;line-height:16px}
.info dt{float:left;clear:left;width:48px;font-weight:700;color:#222}
.info dd{margin-left:48px;color:#444}
.info dd.price{color:var(--blue-title);font-weight:700}
/* footer */
.footer{left:0;top:732px;width:1200px;height:154px;background:var(--navy)}
.foot-bottom{left:0;top:886px;width:1200px;height:38px;background:var(--navy-deep);text-align:center;font-size:11px;color:#6f87ab;line-height:38px}
.f-head{font-size:14px;color:var(--muted);text-transform:uppercase}
.f-list{list-style:none;font-size:13px;color:var(--foot-link);line-height:20.7px}
.f-list li::before{content:"";display:inline-block;border-left:4px solid var(--foot-link);border-top:3px solid transparent;border-bottom:3px solid transparent;margin-right:5px;vertical-align:1px}
.f-div{left:598px;top:745px;width:1px;height:115px;background:rgba(255,255,255,.12)}
.f-text{font-size:13px;color:var(--foot-link);line-height:21px}
.f-text a{color:var(--foot-link)}
</style>
</head>
<body>
<div class="canvas">
  <div class="map-bg" role="img" aria-label="Mapa de regiões ao fundo, em tons claros"></div>

  <div class="abs top-links">Login<span>I</span>Help</div>

  <!-- sidebar -->
  <div class="abs sidebar-shadow"></div>
  <aside class="abs sidebar"></aside>
  <div class="abs brand"><span class="brand-mark"></span><span class="brand-name">Casalúmen</span></div>
  <ul class="abs side-menu">
    <li>A empresa</li><li>Localizacao</li><li>Area Restrita</li><li>Fale Conosco</li>
    <li>Cadastre seu imovel</li><li>Informacoes ao Proprietario</li><li>Informacoes ao Locatario</li><li>Solicite seu imovel</li>
  </ul>
  <div class="abs side-divider"></div>
  <svg class="abs phone-icon" width="40" height="38" viewBox="0 0 40 38" aria-hidden="true">
    <path d="M2 10 C2 2 38 2 38 10 L38 13 L29 13 L29 9 C24 7 16 7 11 9 L11 13 L2 13 Z" fill="#fff"/>
    <g fill="#fff"><circle cx="13" cy="20" r="2.3"/><circle cx="20" cy="20" r="2.3"/><circle cx="27" cy="20" r="2.3"/>
    <circle cx="13" cy="27" r="2.3"/><circle cx="20" cy="27" r="2.3"/><circle cx="27" cy="27" r="2.3"/>
    <circle cx="13" cy="34" r="2.3"/><circle cx="20" cy="34" r="2.3"/><circle cx="27" cy="34" r="2.3"/></g>
  </svg>
  <div class="abs phones">(48) 321 45 90<br>(48) 8712 3305</div>

  <!-- search -->
  <section class="abs search"></section>
  <div class="abs s-title" style="left:426px;top:40px">Busca de imóveis</div>
  <div class="abs field" style="left:425px;top:67px;width:184px">Todos<span class="caret" style="border:0"></span></div>
  <div class="abs check on" style="left:638px;top:72px"></div>
  <div class="abs label" style="left:662px;top:71px">Para comprar</div>
  <div class="abs check" style="left:769px;top:72px"></div>
  <div class="abs label" style="left:794px;top:71px">Para alugar</div>
  <div class="abs btn" style="left:917px;top:66px;width:104px">
    <svg width="17" height="15" viewBox="0 0 17 15" aria-hidden="true"><circle cx="11" cy="6" r="4.5" fill="none" stroke="#fff" stroke-width="2.2"/><path d="M7.5 9 L2 13.5" stroke="#fff" stroke-width="3" stroke-linecap="round"/></svg>Buscar</div>
  <div class="abs s-sep"></div>
  <div class="abs s-title" style="left:426px;top:127px">Busca Avançada</div>

  <div class="abs label" style="left:427px;top:157px">Código:</div>
  <div class="abs field" style="left:480px;top:153px;width:132px">Todos</div>
  <div class="abs label" style="left:625px;top:157px">Tipo:</div>
  <div class="abs field" style="left:673px;top:153px;width:132px"><span class="caret"></span></div>
  <div class="abs label" style="left:822px;top:157px">Endereço:</div>
  <div class="abs field" style="left:889px;top:153px;width:132px"></div>

  <div class="abs label" style="left:427px;top:193px">Bairro:</div>
  <div class="abs field" style="left:480px;top:188px;width:132px">Todos</div>
  <div class="abs label" style="left:625px;top:192px">Cidade:</div>
  <div class="abs field" style="left:673px;top:188px;width:132px"></div>
  <div class="abs label" style="left:822px;top:192px">Região:</div>
  <div class="abs field" style="left:889px;top:188px;width:132px"></div>

  <div class="abs check on" style="left:430px;top:234px"></div>
  <div class="abs label" style="left:453px;top:233px">Save my property</div>
  <div class="abs btn" style="left:890px;top:226px;width:131px">
    <svg width="17" height="15" viewBox="0 0 17 15" aria-hidden="true"><circle cx="11" cy="6" r="4.5" fill="none" stroke="#fff" stroke-width="2.2"/><path d="M7.5 9 L2 13.5" stroke="#fff" stroke-width="3" stroke-linecap="round"/></svg>Procurar</div>

  <!-- results -->
  <div class="abs results-bar"><b>CONTINENTE:</b> Foram encontrados 6 imóveis:</div>

  <article class="abs card" style="left:398px;top:319px">
    <div class="photo"><div role="img" aria-label="Foto de prédio de apartamentos com palmeiras"></div>
      <svg class="ribbon" width="72" height="44" viewBox="0 0 72 44" aria-hidden="true"><polygon points="0,0 26,0 72,26 72,44" fill="#2b8fd6"/><text x="40" y="17" fill="#fff" font-size="8" font-family="Open Sans,sans-serif" font-weight="700" transform="rotate(30 40 17)">NEW</text></svg></div>
    <dl class="info"><dt>Código:</dt><dd>A00687</dd><dt>Tipo:</dt><dd>Apartamento</dd><dt>Quart.:</dt><dd>3</dd><dt>Bairro:</dt><dd>Capoeiras</dd><dt>Cidade:</dt><dd>Florianopolis</dd><dt>Valor:</dt><dd class="price">R$ 970,00</dd></dl>
  </article>
  <article class="abs card" style="left:740px;top:319px">
    <div class="photo"><div role="img" aria-label="Foto de prédio de apartamentos com palmeiras"></div>
      <svg class="ribbon" width="72" height="44" viewBox="0 0 72 44" aria-hidden="true"><polygon points="0,0 26,0 72,26 72,44" fill="#2b8fd6"/><text x="40" y="17" fill="#fff" font-size="8" font-family="Open Sans,sans-serif" font-weight="700" transform="rotate(30 40 17)">NEW</text></svg></div>
    <dl class="info"><dt>Código:</dt><dd>A00687</dd><dt>Tipo:</dt><dd>Apartamento</dd><dt>Quart.:</dt><dd>3</dd><dt>Bairro:</dt><dd>Capoeiras</dd><dt>Cidade:</dt><dd>Florianopolis</dd><dt>Valor:</dt><dd class="price">R$ 970,00</dd></dl>
  </article>
  <article class="abs card" style="left:398px;top:454px">
    <div class="photo"><div role="img" aria-label="Foto de prédio de apartamentos com palmeiras"></div></div>
    <dl class="info"><dt>Código:</dt><dd>A00687</dd><dt>Tipo:</dt><dd>Apartamento</dd><dt>Quart.:</dt><dd>3</dd><dt>Bairro:</dt><dd>Capoeiras</dd><dt>Cidade:</dt><dd>Florianopolis</dd><dt>Valor:</dt><dd class="price">R$ 970,00</dd></dl>
  </article>
  <article class="abs card active" style="left:740px;top:454px">
    <div class="photo"><div role="img" aria-label="Foto de prédio de apartamentos com palmeiras"></div></div>
    <dl class="info"><dt>Código:</dt><dd>A00687</dd><dt>Tipo:</dt><dd>Apartamento</dd><dt>Quart.:</dt><dd>3</dd><dt>Bairro:</dt><dd>Capoeiras</dd><dt>Cidade:</dt><dd>Florianopolis</dd><dt>Valor:</dt><dd class="price">R$ 970,00</dd></dl>
  </article>
  <article class="abs card" style="left:398px;top:591px">
    <div class="photo"><div role="img" aria-label="Foto de prédio de apartamentos com palmeiras"></div></div>
    <dl class="info"><dt>Código:</dt><dd>A00687</dd><dt>Tipo:</dt><dd>Apartamento</dd><dt>Quart.:</dt><dd>3</dd><dt>Bairro:</dt><dd>Capoeiras</dd><dt>Cidade:</dt><dd>Florianopolis</dd><dt>Valor:</dt><dd class="price">R$ 970,00</dd></dl>
  </article>
  <article class="abs card" style="left:740px;top:591px">
    <div class="photo"><div role="img" aria-label="Foto de prédio de apartamentos com palmeiras"></div></div>
    <dl class="info"><dt>Código:</dt><dd>A00687</dd><dt>Tipo:</dt><dd>Apartamento</dd><dt>Quart.:</dt><dd>3</dd><dt>Bairro:</dt><dd>Capoeiras</dd><dt>Cidade:</dt><dd>Florianopolis</dd><dt>Valor:</dt><dd class="price">R$ 970,00</dd></dl>
  </article>

  <!-- footer -->
  <footer class="abs footer"></footer>
  <div class="abs f-head" style="left:157px;top:746px">Menu</div>
  <ul class="abs f-list" style="left:158px;top:772px"><li>A empresa</li><li>Localização</li><li>Área Restrita</li><li>Fale Conosco</li></ul>
  <ul class="abs f-list" style="left:272px;top:772px"><li>Cadastre seu imóvel</li><li>Informações ao Proprietário</li><li>Informações ao Locatário</li><li>Solicite seu imóvel</li></ul>
  <div class="abs f-head" style="left:465px;top:746px">Customers</div>
  <ul class="abs f-list" style="left:465px;top:772px"><li>Privacy</li><li>Terms of use</li><li>Contact Support</li><li>FAQ</li></ul>
  <div class="abs f-div"></div>
  <div class="abs f-head" style="left:619px;top:746px">Contact</div>
  <div class="abs f-text" style="left:621px;top:772px"><span style="font-size:14px;font-weight:600">Casalúmen</span><br>Rua das Acácias, 48<br>Esquina com a Rua Marcos Vilela<br>Centro - Florianópolis</div>
  <div class="abs f-text" style="left:841px;top:771px">CEP :<br>Fax :<br>Locação :<br>Email :</div>
  <div class="abs f-text" style="left:908px;top:771px">88015-310<br>(48) 3344-1276<br>(48) 3219-5502<br><a>contato@casalumen.com</a></div>
  <div class="abs foot-bottom">© (C) 2013 - Casalúmen - Todos os direitos reservados.</div>
</div>
</body>
</html>
```